Harborline Supply Company Business Card Design

The Business Card will be one side only with Harborline Supplies Company Logo
Card should have:
Name
Title
Office phone Number
Cell Number
email address
Website
Street Address
Our Slogan is Rugged and Reliable
Looking for something that stands out from other business cards

Target Market(s)

Heavy equipment Lease Company

```html
<!DOCTYPE html>
<html lang="en">
<head>
<meta charset="utf-8">
<title>Harborline Supplies Company – Business Card</title>
<link rel="stylesheet" href="https://fonts.googleapis.com/css2?family=Roboto:ital,wght@0,400;0,500;0,700;1,700&display=swap">
<style>
  :root {
    --navy: #2e2c74;
    --navy-soft: #3a3884;
    --red: #d11f2e;
    --ink: #222226;
    --paper: #ffffff;
    --backdrop: #e9e6e0;
    --rule: #2b2b2b;
  }
  * { box-sizing: border-box; margin: 0; padding: 0; }
  html, body { width: 900px; height: 1200px; overflow: hidden; }
  body {
    background: var(--backdrop);
    font-family: "Roboto", Arial, sans-serif;
    color: var(--ink);
    position: relative;
  }
  .card {
    position: absolute;
    left: 80px;
    width: 738px;
    height: 432px;
    overflow: hidden;
    box-shadow: 0 6px 14px rgba(0,0,0,0.25);
  }
  .card-front {
    top: 135px;
    background: var(--paper);
    border-radius: 0 46px 0 46px;
  }
  .card-back {
    top: 643px;
    background: var(--navy);
    border-radius: 46px 0 46px 0;
  }
  .brand-name {
    position: absolute;
    left: 0; right: 0;
    top: 88px;
    text-align: center;
    font-weight: 700;
    font-size: 34px;
    letter-spacing: 1px;
    color: var(--red);
    text-transform: uppercase;
  }
  .brand-name .brand-dot {
    display: inline-block;
    width: 26px; height: 26px;
    border-radius: 50%;
    background: var(--navy);
    vertical-align: -3px;
    margin-right: 16px;
  }
  .person-name {
    position: absolute;
    left: 38px; top: 212px;
    font-size: 24px;
    font-weight: 700;
    color: var(--navy);
  }
  .person-title {
    position: absolute;
    right: 40px; top: 216px;
    font-size: 17px;
    color: var(--red);
  }
  .divider {
    position: absolute;
    left: 38px; right: 40px; top: 246px;
    height: 2px;
    background: var(--rule);
  }
  .contact-list {
    position: absolute;
    left: 38px; top: 260px;
    list-style: none;
    font-size: 16px;
    line-height: 26px;
  }
  .contact-list li { display: flex; align-items: center; }
  .contact-list svg { width: 16px; height: 16px; margin-right: 12px; flex: none; }
  .address {
    position: absolute;
    right: 40px; top: 260px;
    text-align: right;
    font-size: 16px;
    line-height: 26px;
  }
  .slogan-band {
    position: absolute;
    left: 0; right: 0; bottom: 0;
    height: 37px;
    background: var(--navy);
    color: #fff;
    text-align: center;
    font-style: italic;
    font-weight: 700;
    font-size: 17px;
    letter-spacing: 0.5px;
    line-height: 37px;
    text-transform: uppercase;
  }
  .slogan-accent {
    position: absolute;
    right: 0; bottom: 20px;
    width: 130px; height: 17px;
    background: var(--red);
    clip-path: polygon(0 0, 100% 0, 100% 100%, 14% 100%);
  }
  .back-pattern {
    position: absolute;
    inset: 0;
    background: linear-gradient(160deg, var(--navy-soft), var(--navy));
  }
  .back-brand {
    position: absolute;
    right: 52px; bottom: 60px;
    font-weight: 700;
    font-size: 16px;
    color: #fff;
    text-transform: uppercase;
    letter-spacing: 0.5px;
  }
</style>
</head>
<body>

<section class="card card-front">
  <div class="brand-name"><span class="brand-dot"></span>Harborline Supplies Company</div>

  <h1 class="person-name">Daniel Mercer</h1>
  <p class="person-title">Director of Sales &amp; Marketing</p>
  <div class="divider"></div>

  <ul class="contact-list">
    <li>
      <svg viewBox="0 0 16 16"><path fill="var(--red)" d="M3.5 1.5l2.5 2.8-1.4 1.8c.9 2 2.5 3.6 4.5 4.5l1.8-1.4 2.8 2.5-1.6 2.3C7 13.5 2.5 9 1.2 3.1z"/></svg>
      (555)310-4826
    </li>
    <li>
      <svg viewBox="0 0 16 16"><rect x="3.5" y="1" width="9" height="14" rx="1.5" fill="none" stroke="var(--red)" stroke-width="1.6"/><circle cx="8" cy="12.3" r="1" fill="var(--red)"/></svg>
      (555)274-9051
    </li>
    <li>
      <svg viewBox="0 0 16 16"><rect x="1" y="3" width="14" height="10" fill="var(--red)"/><path d="M1.5 3.5L8 9l6.5-5.5" fill="none" stroke="#fff" stroke-width="1.3"/></svg>
      info@harborlinesupply.com
    </li>
    <li>
      <svg viewBox="0 0 16 16" fill="none" stroke="var(--red)" stroke-width="1.3"><circle cx="8" cy="8" r="6.5"/><ellipse cx="8" cy="8" rx="2.8" ry="6.5"/><path d="M1.5 8h13M2.5 4.8h11M2.5 11.2h11"/></svg>
      www.HarborlinePumps.com
    </li>
  </ul>

  <address class="address" style="font-style:normal">
    1400, 215 Quay Street West<br>
    Port Avery, NS, B3X 4K7
  </address>

  <div class="slogan-accent"></div>
  <div class="slogan-band">Rugged and Reliable</div>
</section>

<section class="card card-back">
  <div class="back-pattern" role="img" aria-label="Repeating tone-on-tone brand emblem pattern on navy"></div>
  <div class="back-brand">Harborline Supplies Company</div>
</section>

</body>
</html>
```